Norvel Hand Wash

Design hand washes. Total 12 variants to be designed.

Variants name are:

1) MILK &OLIVE
2) Shea Butter
3) Hidden Dawn
4) Cream and Peach
5) Milk and Honey
6) Amber Whisper
7) Bakhour
8) Musk
9) White Oud
10) Black Oud
11) Rose Oud
12) Oud & Sandalwood

Labels can be on transparent sticker or background colors. All variants will be differentiated by fragrances and color. Bottle will be transparent. Pumps used for dispensing will be in Black or Transparent Color.

Designers can initially present designs of 4-5 variants initially. Later based on feedback, they can work out on more.

Bottle is 400ml and shape is rectangle. Ignore the size on bottle picture. Bottle keyline is attached.

Target Market(s)

B+, B, C+

Requirements
Must have
• Some relation to the variant names

```html
<!DOCTYPE html>
<html lang="en">
<head>
<meta charset="utf-8">
<title>Norvel Hand Wash – Label Range</title>
<link rel="stylesheet" href="https://fonts.googleapis.com/css2?family=Berkshire+Swash&family=Lora:ital,wght@0,600;1,400&family=Arimo&display=swap">
<style>
  :root {
    --canvas: #ffffff;
    --hand-wash: #6b5aa8;
    --brand-ink: #5b4a9c;
    --badge: #ffffff;
    --size-ink: #4a4a4a;
    --pump: #e4e6ea;
    --bottle-edge: #c9ced6;
    --bottle-fill: rgba(225, 230, 238, 0.35);

    --rose-art: #f7d9e6;  --rose-band: #b33a62;  --rose-title: #a8325a;
    --rose-low-a: #fdeef3; --rose-low-b: #f8d2e1;
    --honey-art: #f3a53a; --honey-band: #7b3a1a; --honey-title: #6e2f14;
    --honey-low-a: #fde7c6; --honey-low-b: #f6b561;
    --amber-art: #e3f0f8; --amber-band: #4e2e25; --amber-title: #4a2a20;
    --amber-low-a: #fcf9ea; --amber-low-b: #e9ddb5;
    --olive-art: #d7e6b4; --olive-band: #3f5a24; --olive-title: #34491c;
    --olive-low-a: #f6f8e2; --olive-low-b: #a9c87a;
  }
  * { box-sizing: border-box; margin: 0; padding: 0; }
  html, body { width: 1200px; height: 1000px; overflow: hidden; background: var(--canvas); }
  .range { position: relative; width: 1200px; height: 1000px; }

  .label {
    position: absolute; overflow: hidden; border-radius: 2em;
    background: linear-gradient(180deg, var(--low-a), var(--low-b));
    font-size: 10px; text-align: center;
  }
  .label--small { font-size: 5px; }
  .label__art { position: absolute; left: 0; top: 0; width: 100%; height: 56%; background: var(--art); }
  .label__motif {
    position: absolute; left: 50%; top: 8%; width: 13em; height: 11em; transform: translateX(-50%);
    border-radius: 1.5em; background: var(--motif); opacity: .85;
  }
  .label__band { position: absolute; left: 0; top: 56%; width: 100%; height: 5.4%; background: var(--band); }
  .label__brand {
    position: absolute; left: 50%; top: 51.5%; transform: translateX(-50%);
    width: 9em; height: 5.2em; border-radius: 1em; background: var(--badge);
    display: flex; align-items: center; justify-content: center;
    font-family: "Lora", serif; font-weight: 600; font-size: 1em; color: var(--brand-ink);
  }
  .label__brand span { font-size: 2.6em; }
  .label__name {
    position: absolute; left: 0; width: 100%; top: 71.5%;
    font-family: "Berkshire Swash", cursive; font-size: 3.3em; color: var(--title); white-space: nowrap;
  }
  .label__kind {
    position: absolute; left: 0; width: 100%; top: 79%;
    font-family: "Lora", serif; font-style: italic; font-size: 1.9em; color: var(--hand-wash);
  }
  .label__size {
    position: absolute; left: 0; width: 100%; top: 93.5%;
    font-family: "Arimo", sans-serif; font-size: 1.2em; color: var(--size-ink);
  }

  .rose  { --art: var(--rose-art);  --band: var(--rose-band);  --title: var(--rose-title);  --low-a: var(--rose-low-a);  --low-b: var(--rose-low-b);  --motif: #d9667f; }
  .honey { --art: var(--honey-art); --band: var(--honey-band); --title: var(--honey-title); --low-a: var(--honey-low-a); --low-b: var(--honey-low-b); --motif: #f6e3c4; }
  .amber { --art: var(--amber-art); --band: var(--amber-band); --title: var(--amber-title); --low-a: var(--amber-low-a); --low-b: var(--amber-low-b); --motif: #d8c7a0; }
  .olive { --art: var(--olive-art); --band: var(--olive-band); --title: var(--olive-title); --low-a: var(--olive-low-a); --low-b: var(--olive-low-b); --motif: #eef2e0; }

  .bottle { position: absolute; }
  .bottle__pump { position: absolute; left: 0; top: 0; border-radius: 8px 8px 4px 4px; background: var(--pump); }
  .bottle__body {
    position: absolute; border: 2px solid var(--bottle-edge); border-radius: 34px 34px 22px 22px;
    background: var(--bottle-fill);
  }
</style>
</head>
<body>
<main class="range">

  <!-- Rose Oud: flat label -->
  <section class="label rose" style="left:25px;top:32px;width:272px;height:480px;">
    <div class="label__art" role="img" aria-label="Soft pink floral pattern background"></div>
    <div class="label__motif" role="img" aria-label="Illustration of pink roses with leaves"></div>
    <div class="label__band"></div>
    <div class="label__brand"><span>Norvel</span></div>
    <h2 class="label__name">Rose Oud</h2>
    <p class="label__kind">Hand Wash</p>
    <p class="label__size">400 mL (13.5 fl. oz.)</p>
  </section>

  <!-- Rose Oud: bottle -->
  <div class="bottle" style="left:372px;top:65px;">
    <div class="bottle__pump" role="img" aria-label="Clear dispensing pump" style="width:118px;height:90px;"></div>
    <div class="bottle__body" style="left:0;top:88px;width:158px;height:347px;"></div>
  </div>
  <section class="label label--small rose" style="left:385px;top:185px;width:134px;height:245px;">
    <div class="label__art" role="img" aria-label="Soft pink floral pattern background"></div>
    <div class="label__motif" role="img" aria-label="Illustration of pink roses with leaves"></div>
    <div class="label__band"></div>
    <div class="label__brand"><span>Norvel</span></div>
    <h2 class="label__name">Rose Oud</h2>
    <p class="label__kind">Hand Wash</p>
    <p class="label__size">400 mL (13.5 fl. oz.)</p>
  </section>

  <!-- Milk & Honey: flat label -->
  <section class="label honey" style="left:608px;top:32px;width:272px;height:480px;">
    <div class="label__art" role="img" aria-label="Golden honeycomb pattern background"></div>
    <div class="label__motif" role="img" aria-label="Illustration of a honey jar and a milk bottle"></div>
    <div class="label__band"></div>
    <div class="label__brand"><span>Norvel</span></div>
    <h2 class="label__name">Milk &amp; Honey</h2>
    <p class="label__kind">Hand Wash</p>
    <p class="label__size">400 mL (13.5 fl. oz.)</p>
  </section>

  <!-- Milk & Honey: bottle -->
  <div class="bottle" style="left:955px;top:60px;">
    <div class="bottle__pump" role="img" aria-label="Clear dispensing pump" style="width:108px;height:92px;"></div>
    <div class="bottle__body" style="left:0;top:90px;width:160px;height:285px;"></div>
  </div>
  <section class="label label--small honey" style="left:967px;top:195px;width:136px;height:225px;">
    <div class="label__art" role="img" aria-label="Golden honeycomb pattern background"></div>
    <div class="label__motif" role="img" aria-label="Illustration of a honey jar and a milk bottle"></div>
    <div class="label__band"></div>
    <div class="label__brand"><span>Norvel</span></div>
    <h2 class="label__name">Milk &amp; Honey</h2>
    <p class="label__kind">Hand Wash</p>
    <p class="label__size">400 mL (13.5 fl. oz.)</p>
  </section>

  <!-- Amber Whisper: bottle -->
  <div class="bottle" style="left:75px;top:545px;">
    <div class="bottle__pump" role="img" aria-label="Clear dispensing pump" style="width:115px;height:88px;"></div>
    <div class="bottle__body" style="left:0;top:86px;width:165px;height:344px;"></div>
  </div>
  <section class="label label--small amber" style="left:90px;top:690px;width:135px;height:238px;">
    <div class="label__art" role="img" aria-label="Pale blue damask pattern background"></div>
    <div class="label__motif" role="img" aria-label="Illustration of a vanilla flower and pods with a magnifying glass"></div>
    <div class="label__band"></div>
    <div class="label__brand"><span>Norvel</span></div>
    <h2 class="label__name">Amber Whisper</h2>
    <p class="label__kind">Hand Wash</p>
    <p class="label__size">400 mL (13.5 fl. oz.)</p>
  </section>

  <!-- Amber Whisper: flat label -->
  <section class="label amber" style="left:318px;top:470px;width:270px;height:485px;">
    <div class="label__art" role="img" aria-label="Pale blue damask pattern background"></div>
    <div class="label__motif" role="img" aria-label="Illustration of a vanilla flower and pods with a magnifying glass"></div>
    <div class="label__band"></div>
    <div class="label__brand"><span>Norvel</span></div>
    <h2 class="label__name">Amber Whisper</h2>
    <p class="label__kind">Hand Wash</p>
    <p class="label__size">400 mL (13.5 fl. oz.)</p>
  </section>

  <!-- Milk & Olive: bottle -->
  <div class="bottle" style="left:665px;top:545px;">
    <div class="bottle__pump" role="img" aria-label="Clear dispensing pump" style="width:115px;height:88px;"></div>
    <div class="bottle__body" style="left:0;top:86px;width:155px;height:344px;"></div>
  </div>
  <section class="label label--small olive" style="left:680px;top:670px;width:126px;height:280px;">
    <div class="label__art" role="img" aria-label="Light green olive branch pattern background"></div>
    <div class="label__motif" role="img" aria-label="Illustration of a milk bottle with an olive branch"></div>
    <div class="label__band"></div>
    <div class="label__brand"><span>Norvel</span></div>
    <h2 class="label__name">Milk &amp; Olive</h2>
    <p class="label__kind">Hand Wash</p>
    <p class="label__size">400 mL (13.5 fl. oz.)</p>
  </section>

  <!-- Milk & Olive: flat label -->
  <section class="label olive" style="left:900px;top:477px;width:268px;height:478px;">
    <div class="label__art" role="img" aria-label="Light green olive branch pattern background"></div>
    <div class="label__motif" role="img" aria-label="Illustration of a milk bottle with an olive branch"></div>
    <div class="label__band"></div>
    <div class="label__brand"><span>Norvel</span></div>
    <h2 class="label__name">Milk &amp; Olive</h2>
    <p class="label__kind">Hand Wash</p>
    <p class="label__size">400 mL (13.5 fl. oz.)</p>
  </section>

</main>
</body>
</html>
```